Unique Book Cover for Colors (Front, Spine Back and 1 page spread for inside)

We are looking for a creative design for book cover with harmonious colors.
It should be contemporary, stylish and clean that will grab the attention of the clients.

Must have a unique layout perhaps consisting of:

- Beautiful sceneries of nature
- Anything inspired from nature
- Which also has a well planned and thought of color combination.

Must:

1. Use the size w = 14.5cm xh = 20cm spine = 6cm.

2. Logo must be in the upper middle. (See attachment)

3. Front and back cover must have a meaning. We would like it to come across as serious and professional, yet very personable and modern.(unique front & back cover)

4. Create a text "Tint Harbor" (front and spine only)

5. Also attached is the template for the inside spread page. Use that as a reference for your creative idea.

6. Please use the attached text (address)for the back cover. (must be in the middle bottom of the page).

7. Design must invoke a sense of peaceful emotion

8. Overall design must not be cluttered.

History of the Company
Al-Noor Coatings Company, was established in Riyadh, the capital of the Kingdom of Saudi Arabia, in 1979, as a small company with high aspirations and ambitions. In a short period of time, and as a result of the vision and dedication of the founders, the efforts have succeeded in laying strong grounds for a pioneering company in the paint industry in the GCC countries and the Middle East at large. In this context, the company became a pioneer in manufacturing and developing innovative, high quality and environmentally responsible paints, designed to meet the requirements and needs of a wide range of clients including industrial, commercial and individuals.

Looking forward to see your creative ideas....

ENJOY!!

Target Market(s)

Corporate, Urban, Real Estate

Industry/Entity Type

Paint

Font styles to use
Serif
Sans Serif
Decorative
Script
Other font styles liked:
• Arial, Helvetica thin 35

Requirements
Must have
• 1. Use the size w = 14.5cm xh = 20cm spine = 6cm.

Should not have
• people and animals

```html
<!DOCTYPE html>
<html lang="en">
<head>
<meta charset="utf-8">
<title>Tint Harbor – Book Cover</title>
<link href="https://fonts.googleapis.com/css2?family=Raleway:ital,wght@0,200;0,400;1,400&family=Roboto:wght@700&family=Amiri&display=swap" rel="stylesheet">
<style>
  :root{
    --paper:#e2e2dc;
    --spine-red:#e2343c;
    --title-red:#d9303d;
    --ink:#1e1e1e;
    --spine-ink:#f2efe6;
    --blue:#4f8fd8;
    --green:#5fbf70;
    --yellow:#e8e43a;
    --red:#e03a34;
    --badge:#55476a;
    --icon:#c23b2e;
  }
  *{margin:0;padding:0;box-sizing:border-box}
  html,body{width:1200px;height:710px;overflow:hidden;background:var(--paper)}
  .cover{position:relative;width:1200px;height:710px;background:var(--paper);font-family:"Raleway",Arial,sans-serif}

  /* back cover */
  .back{position:absolute;left:0;top:0;width:518px;height:710px}
  .flower-art{position:absolute;left:0;top:0;width:445px;height:545px;
    border-bottom-right-radius:60% 45%;
    background:
      radial-gradient(circle at 100px 430px,var(--red) 0 95px,transparent 110px),
      radial-gradient(circle at 250px 350px,var(--yellow) 0 150px,transparent 175px),
      radial-gradient(circle at 320px 150px,var(--green) 0 140px,transparent 165px),
      radial-gradient(circle at 70px 150px,var(--blue) 0 160px,transparent 190px),
      linear-gradient(160deg,#8fc0e8,#a8d8a8 60%,var(--paper));}
  .partners{position:absolute;left:36px;top:672px;display:flex;gap:5px}
  .partners span{width:17px;height:17px;border-radius:50%;background:var(--badge)}
  .contact{position:absolute;left:150px;top:662px;width:250px}
  .contact .web{font-family:"Roboto",Arial,sans-serif;font-weight:700;font-size:15px;color:var(--ink);letter-spacing:.4px}
  .handles{display:flex;gap:9px;margin-top:6px;font-family:"Roboto",Arial,sans-serif;font-weight:700;font-size:8px;color:var(--ink)}
  .handles span{display:flex;align-items:center;gap:3px}
  .handles i{display:inline-block;width:11px;height:11px;background:var(--icon)}
  .tagline{position:absolute;left:410px;top:666px;width:80px;text-align:center;color:var(--ink)}
  .tagline .ar{font-family:"Amiri",serif;font-size:14px;line-height:15px}
  .tagline .en{font-family:"Raleway",Arial,sans-serif;font-style:italic;font-size:9px;margin-top:2px}

  /* spine */
  .spine{position:absolute;left:518px;top:0;width:165px;height:710px;background:var(--spine-red)}
  .spine-brush{position:absolute;left:34px;top:0;width:88px;height:710px;
    background:linear-gradient(90deg,#c9803a,#7f9a3a 35%,#6f9a3c 60%,#d7703a)}
  .spine-title{position:absolute;left:80px;top:355px;transform:translate(-50%,-50%) rotate(90deg);
    white-space:nowrap;font-weight:200;font-size:90px;letter-spacing:6px;color:transparent;
    -webkit-text-stroke:1.3px var(--spine-ink)}

  /* front cover */
  .front{position:absolute;left:683px;top:0;width:517px;height:710px}
  .front-title{position:absolute;left:10px;top:64px;display:flex;align-items:center;gap:12px;
    font-weight:400;font-size:48px;letter-spacing:1px;color:var(--title-red)}
  .front-title .dot{width:40px;height:40px;border-radius:50%;background:var(--title-red)}
  .crane-art{position:absolute;left:0;top:150px;width:517px;height:560px;
    clip-path:polygon(0 0,30% 0,60% 25%,100% 55%,100% 100%,0 100%);
    background:linear-gradient(170deg,var(--yellow) 0%,#6fae3a 18%,#3d62d4 42%,#d9353a 68%,#e0b840 100%)}
</style>
</head>
<body>
<main class="cover">
  <section class="back">
    <div class="flower-art" role="img" aria-label="Layered paper flowers in blue, green, yellow and red"></div>
    <div class="partners"><span></span><span></span><span></span><span></span></div>
    <div class="contact">
      <p class="web">www.alnoorcoatings.com</p>
      <p class="handles"><span><i></i>alnoorcoatings</span><span><i></i>alnoorcoatingsCo</span><span><i></i>alnoorcoatings</span></p>
    </div>
    <div class="tagline"><p class="ar" lang="ar">هدوء ولون</p><p class="en">Calm &amp; Colour</p></div>
  </section>

  <section class="spine">
    <div class="spine-brush"></div>
    <p class="spine-title">TINT HARBOR</p>
  </section>

  <section class="front">
    <h1 class="front-title">TINT <span class="dot"></span> HARBOR</h1>
    <div class="crane-art" role="img" aria-label="Flock of origami paper cranes in yellow, green, blue and red"></div>
  </section>
</main>
</body>
</html>
```